Copper Ridge Grazing Meat Delivery Box

We'd like to have a bison (Canadian buffalo) inspired pattern for our delivery box. I've included examples of pattern style we are looking for. Note I don't want our pattern to have any mention of Beef, Pork, Chicken, etc. We only sell bison meat. :) I was thinking maybe the pattern could be bison inspired with our bison head (image included), barns, mountains, and grass all mixed into a cool look. Just a thought.

'The Larder Guilds' box (picture included) is where we had the idea come from. But less complicated and full of text.

I like the idea of the big black band around the box that would have our company logo and our mantra. "Growing a sustainable future, & eating well along the way."

I'm interested in seeing what sketch hive comes up with or thinks of. If you have another idea show it! However the black band is important and we don't want the pattern to be as busy as the larder guild, filled with so much text, etc.

Please include our social media and website that would be awesome.

Website: copperridgegrazing.ca
Snapgram & Friendsphere: copperridgegrazing

We want to keep it black with the kraft colouring of the box (this is the brown colour a box has).

Fonts styles we us: 'Roboto Condensed', 'HWT American', 'Abadi MT Condensed Light' and 'Raleway'.

Box Dimensions (LxWxH): 16"x12"x10"
However, we want to be able to resize the pattern for any size box if we need too.

Best of luck!
Updates

**Note: For the bison inspired design we are looking for a pattern made up of bison inspired items/images (examples could be: Mountains, fields, bison hooves prints, barns, barbwire fences, the bison head that we included in the logo ai, etc.) Feel free to use your imagination.We don't sell other meat products other then bison so no pigs, chickens, or cows on our box. Thank you! Added Wednesday, July 5, 2017

Target Market(s)

Individuals 21+ that enjoy healthy meat products. People that enjoy entertaining or cooking for family.

Industry/Entity Type

Agriculture

Font styles to use
Other font styles liked:
• 'Roboto Condensed', 'HWT American', 'Akzidenz-Grotesk BQ Condensed', 'Abadi MT Condensed Light' and 'Raleway'.

Colors
1b1b1b
ffffff
9d9d9d
5c5c5c

Requirements
Must have
• Black band around the box that would have our company logo and our mantra. "Growing a sustainable future, & eating well along the way.
• A bison themed pattern. I've included examples of what a pattern is. Note I don't want our pattern to have any mention of Beef, Pork, Chicken, etc. We only sell bison meat. :) I was thinking maybe the pattern could be bison inspired with our bison head (image included), barns, mountains, and grass all mixed into a cool look. Just a thought.
• Where people can find us:
• Website: copperridgegrazing.ca
• Snapgram & Friendsphere: copperridgegrazing
• We'd like to have the ability to have the bison pattern separate to the entire box design if we choose. Then we can use for additional packaging. Ie: Packaging design with the black band and pattern. And then the pattern on it's own.
Nice to have
• Please read must haves and project description.
Should not have
• A busy or clashing pattern. Any mention of Beef, Pork, Chicken, etc. We only sell bison meat. :)

```html
<!DOCTYPE html>
<html lang="en">
<head>
<meta charset="utf-8">
<title>Copper Ridge Grazing – Delivery Box</title>
<link href="https://fonts.googleapis.com/css2?family=Montserrat:wght@600;800;900&family=Kaushan+Script&family=Open+Sans:wght@600&display=swap" rel="stylesheet">
<style>
  :root {
    --kraft: #c9a97c;
    --kraft-dark: #b89668;
    --ink: #1f1c1a;
    --band: #1b1b1b;
    --grey-mid: #5c5c5c;
    --grey-light: #9d9d9d;
    --page: #ececec;
  }
  * { box-sizing: border-box; margin: 0; padding: 0; }
  html, body { width: 1200px; height: 750px; overflow: hidden; }
  body { background: var(--page); font-family: "Montserrat", sans-serif; position: relative; }

  .panel { position: absolute; left: 40px; width: 1120px; background: var(--kraft); overflow: hidden; }
  .panel--lid { top: 30px; height: 440px; }
  .panel--side { top: 490px; height: 230px; }

  .band { position: absolute; top: 0; right: 0; width: 400px; height: 100%; background: var(--band); color: var(--kraft); }

  .art { position: absolute; }
  .art--mountains { background: linear-gradient(180deg, rgba(140,115,85,0), rgba(140,115,85,.4)); }
  .art--grass { background: linear-gradient(180deg, rgba(92,92,92,0), rgba(92,92,92,.6)); }
  .art--scene { border-radius: 8px; background: linear-gradient(180deg, rgba(31,28,26,.78), rgba(31,28,26,.92)); }
  .art--prints { border-radius: 8px; background: rgba(31,28,26,.22); }

  .headline { position: absolute; color: var(--ink); line-height: .9; }
  .headline__bison { font-weight: 900; letter-spacing: 2px; display: block; }
  .headline__pct { font-weight: 800; display: block; }
  .headline__tasty { font-family: "Kaushan Script", cursive; display: block; }

  .lid-headline { left: 48px; top: 30px; }
  .lid-headline .headline__bison { font-size: 62px; }
  .lid-headline .headline__pct { font-size: 22px; margin-top: -4px; }
  .lid-headline .headline__tasty { font-size: 62px; margin: -18px 0 0 44px; }

  .local-farm { position: absolute; font-weight: 800; color: var(--ink); line-height: .9; text-transform: uppercase; }
  .lid-local { left: 600px; top: 250px; font-size: 38px; transform: rotate(-90deg); transform-origin: left top; }

  .natural { position: absolute; line-height: .8; }
  .natural__word { font-weight: 900; display: block; }
  .natural__script { font-family: "Kaushan Script", cursive; display: block; }
  .lid-natural { left: 230px; top: 300px; color: var(--kraft); }
  .lid-natural .natural__word { font-size: 22px; }
  .lid-natural .natural__script { font-size: 20px; margin-left: 14px; }

  .brand { display: flex; align-items: center; justify-content: center; gap: 14px; }
  .brand__mark { width: 40px; height: 40px; border: 3px solid var(--kraft); border-radius: 50%; flex: none; }
  .brand__name { font-weight: 800; font-size: 24px; letter-spacing: 2px; text-transform: uppercase; line-height: 1.1; }

  .lid-brand { position: absolute; top: 60px; left: 30px; right: 30px; }

  .mantra { position: absolute; top: 180px; left: 20px; right: 20px; text-align: center; font-weight: 800; font-size: 27px; line-height: 1.05; letter-spacing: 1px; text-transform: uppercase; }

  .web-pill { position: absolute; top: 350px; left: 60px; right: 60px; height: 34px; border-radius: 17px; background: var(--kraft); color: var(--band); font-family: "Open Sans", sans-serif; font-weight: 600; font-size: 16px; display: flex; align-items: center; justify-content: center; letter-spacing: .5px; }

  .socials { position: absolute; top: 398px; left: 0; right: 0; display: flex; justify-content: center; gap: 22px; font-family: "Open Sans", sans-serif; font-weight: 600; font-size: 14px; }
  .socials__item { display: flex; align-items: center; gap: 6px; }
  .socials__box { width: 14px; height: 14px; background: var(--kraft); }

  .side-headline { left: 180px; top: 30px; }
  .side-headline .headline__bison { font-size: 76px; }
  .side-headline .headline__pct { font-size: 26px; margin-top: -4px; }
  .side-headline .headline__tasty { font-size: 72px; margin: -22px 0 0 80px; }
  .side-local { left: 30px; top: 110px; font-size: 22px; }

  .side-natural { position: absolute; top: 24px; left: 0; right: 0; text-align: center; color: var(--kraft); }
  .side-natural .natural__word { font-size: 50px; letter-spacing: 2px; }
  .side-natural .natural__script { font-size: 36px; margin-top: 4px; }
  .side-brand { position: absolute; top: 150px; left: 20px; right: 20px; }
</style>
</head>
<body>

<section class="panel panel--lid" aria-label="Box lid">
  <div class="art art--mountains" role="img" aria-label="Outline of mountain range behind the field" style="left:140px;top:150px;width:560px;height:180px;"></div>
  <div class="art art--grass" role="img" aria-label="Prairie grass along the ground" style="left:0;top:340px;width:720px;height:100px;"></div>
  <div class="art art--scene" role="img" aria-label="Side-view bison silhouette with dashed cut lines, and a small barbecue grill with flame by its head" style="left:140px;top:200px;width:450px;height:200px;"></div>
  <div class="art art--prints" role="img" aria-label="Scattered bison hoof prints" style="left:530px;top:30px;width:130px;height:70px;"></div>

  <h1 class="headline lid-headline">
    <span class="headline__bison">BISON</span>
    <span class="headline__pct">100%</span>
    <span class="headline__tasty">tasty</span>
  </h1>
  <p class="local-farm lid-local">Local<br>Farm</p>
  <p class="natural lid-natural"><span class="natural__word">Natural</span><span class="natural__script">product</span></p>

  <div class="band">
    <div class="brand lid-brand">
      <span class="brand__mark"></span>
      <span class="brand__name">Copper Ridge<br>Grazing</span>
    </div>
    <p class="mantra">Growing a<br>sustainable<br>future, &amp; eating<br>well along<br>the way.</p>
    <p class="web-pill">www.copperridgegrazing.ca</p>
    <div class="socials">
      <span class="socials__item"><span class="socials__box"></span>copperridgegrazing</span>
      <span class="socials__item"><span class="socials__box"></span>copperridgegrazing</span>
    </div>
  </div>
</section>

<section class="panel panel--side" aria-label="Box side">
  <div class="art art--mountains" role="img" aria-label="Outline of mountain range" style="left:20px;top:40px;width:660px;height:140px;"></div>
  <div class="art art--grass" role="img" aria-label="Prairie grass along the ground" style="left:0;top:160px;width:720px;height:70px;"></div>
  <div class="art art--prints" role="img" aria-label="Scattered bison hoof prints" style="left:40px;top:14px;width:100px;height:70px;"></div>

  <p class="local-farm side-local">Local<br>Farm</p>
  <h2 class="headline side-headline">
    <span class="headline__bison">BISON</span>
    <span class="headline__pct">100%</span>
    <span class="headline__tasty">tasty</span>
  </h2>

  <div class="band">
    <p class="natural side-natural"><span class="natural__word">Natural</span><span class="natural__script">product</span></p>
    <div class="brand side-brand">
      <span class="brand__mark"></span>
      <span class="brand__name">Copper Ridge<br>Grazing</span>
    </div>
  </div>
</section>

</body>
</html>
```